Brisbane IT support business needs our first letterhead (Contest)

Hello we are a Brisbane based Information Technology company providing support and services to small and medium sized businesses. We provide a range of services and solutions.

The business name is Harlowe Network Computing Services, or HNCS for short.

I am looking for a letterhead that looks professional (don't we all want that), but most importantly, it most utilize the colours in the logo attached, and any text used preferably in font type: HandelGotDBol.

```html
<!DOCTYPE html>
<html lang="en">
<head>
<meta charset="utf-8">
<title>HNCS Letterhead</title>
<link href="https://fonts.googleapis.com/css2?family=Michroma&display=swap" rel="stylesheet">
<style>
  :root {
    --backdrop: #e4e4e4;
    --paper: #ffffff;
    --navy: #1d4d6b;
    --orange: #ee7a22;
    --mist: #dfe5e8;
    --rule: #b9bec2;
  }
  * { margin: 0; padding: 0; box-sizing: border-box; }
  html, body {
    width: 1200px;
    height: 1010px;
    overflow: hidden;
    background: var(--backdrop);
  }
  .letterhead {
    position: absolute;
    left: 236px;
    top: 35px;
    width: 727px;
    height: 940px;
    background: var(--paper);
    box-shadow: 0 2px 10px rgba(0,0,0,0.12);
    font-family: "Michroma", sans-serif;
    color: var(--navy);
  }
  .brand {
    position: absolute;
    top: 62px;
    left: 0;
    width: 100%;
    display: flex;
    justify-content: center;
    align-items: center;
    gap: 14px;
  }
  .brand-dot {
    width: 46px;
    height: 46px;
    border-radius: 50%;
    background: var(--navy);
  }
  .brand-text {
    display: flex;
    flex-direction: column;
    border-left: 1px solid var(--orange);
    padding-left: 10px;
  }
  .brand-name {
    font-size: 26px;
    line-height: 1;
    color: var(--orange);
    letter-spacing: 1px;
  }
  .brand-tagline {
    margin-top: 4px;
    font-size: 6px;
    color: var(--navy);
    letter-spacing: 0.3px;
  }
  .backdrop-disc {
    position: absolute;
    left: 163px;
    top: 215px;
    width: 400px;
    height: 400px;
  }
  .footer-rule {
    position: absolute;
    left: 40px;
    right: 40px;
    top: 792px;
    height: 1px;
    background: var(--rule);
  }
  .footer {
    position: absolute;
    left: 40px;
    right: 40px;
    top: 808px;
    display: flex;
    justify-content: space-between;
    font-size: 11px;
    line-height: 1.55;
  }
  .footer-contact { text-align: left; }
  .footer-address { font-size: 12px; }
</style>
</head>
<body>
  <main class="letterhead">
    <header class="brand">
      <div class="brand-dot"></div>
      <div class="brand-text">
        <span class="brand-name">HNCS</span>
        <span class="brand-tagline">Harlowe Network Computing Services</span>
      </div>
    </header>

    <svg class="backdrop-disc" viewBox="0 0 400 400" aria-hidden="true">
      <circle cx="200" cy="200" r="200" fill="var(--mist)"/>
    </svg>

    <div class="footer-rule"></div>
    <footer class="footer">
      <address class="footer-address" style="font-style:normal">
        418 Larkspur Row, Suite 310<br>
        Milton, Queensland 4064
      </address>
      <div class="footer-contact">
        Telephone: 000-000-0000 | Movil 000-000-0000<br>
        www.harlowencs.com
      </div>
    </footer>
  </main>
</body>
</html>
```